Commercial construction contractor website.

We need a website that contains About Us, Contact info, Services, Project pictures and Industry News section

Target Market(s)

I'm building industral/flex spaces/commercial.

Industry/Entity Type

Commercial/industrial construction

Coding

Coded - Design and coding required

Number of Pages Required

5+ page

Font styles to use
Other font styles liked:
• The logo font is Microgramma Pro

Requirements
Must have
• Must have correct company name spelling: Halvern Ridge Construction
Nice to have
• I do like to see our logo design implemented in the design
Should not have
• Please do not show big city pictures and business suit people. We are a commercial construction company

```html
<!DOCTYPE html>
<html lang="en">
<head>
<meta charset="utf-8">
<title>Halvern Ridge Construction</title>
<link rel="stylesheet" href="https://fonts.googleapis.com/css2?family=Orbitron:wght@700;800&family=Roboto:wght@400;500;700&display=swap">
<style>
:root{
  --blue:#0d4fa3;
  --blue-bright:#1a6fd1;
  --navy:#0b3a7a;
  --ink:#1b1b1b;
  --text:#333;
  --light:#f0f0f0;
  --white:#fff;
  --grey-btn:#8d8d8d;
}
*{box-sizing:border-box;margin:0;padding:0}
html,body{width:1200px;height:4878px;overflow:hidden}
body{position:relative;font-family:"Roboto",Arial,sans-serif;color:var(--text);background:var(--white)}
.abs{position:absolute}
.display{font-family:"Orbitron",Arial,sans-serif;font-weight:800}
.btn{position:absolute;display:flex;align-items:center;justify-content:center;background:var(--blue);color:var(--white);font-family:"Orbitron",Arial,sans-serif;font-weight:800;font-size:18px}

/* header */
.site-header{position:absolute;left:0;top:0;width:1200px;height:142px;background:var(--white);z-index:3}
.call{left:94px;top:32px;font-family:"Orbitron",Arial,sans-serif;font-weight:700;font-size:18px;color:var(--blue-bright)}
.quote-btn{left:909px;top:22px;width:190px;height:42px;font-size:14px}
.nav{top:93px;display:flex;gap:28px;font-family:"Orbitron",Arial,sans-serif;font-weight:700;font-size:14px;color:var(--ink)}
.nav .active{color:var(--blue-bright)}
.nav-left{left:98px}
.nav-right{left:782px}
.brand-tab{position:absolute;left:466px;top:0;width:292px;height:206px;background:var(--white);clip-path:polygon(0 0,100% 0,100% 75%,92% 100%,8% 100%,0 75%);z-index:4;display:flex;align-items:flex-end;justify-content:center;padding-bottom:24px}
.brand-name{font-family:"Orbitron",Arial,sans-serif;font-weight:700;font-size:18px;color:#7a7a7a;text-align:center;line-height:1.3}

/* hero */
.hero{left:0;top:142px;width:1200px;height:619px;background:linear-gradient(180deg,#3b4451 0%,#57606a 45%,#6d6b4c 70%,#3e3f35 100%)}
.hero h1{position:absolute;left:0;width:1200px;top:240px;text-align:center;font-family:"Orbitron",Arial,sans-serif;font-weight:800;font-size:50px;line-height:62px;color:var(--white)}
.hero p{position:absolute;left:0;width:1200px;top:370px;text-align:center;font-size:15px;line-height:20px;color:var(--white)}
.hero .btn{left:498px;top:420px;width:206px;height:48px}
.hero .arrow{position:absolute;top:340px}

/* about */
.about-photo{left:110px;top:852px;width:405px;height:354px;background:linear-gradient(135deg,#8a8c92,#4f5963 60%,#7a6b58);clip-path:polygon(25% 0,75% 0,100% 50%,75% 100%,25% 100%,0 50%)}
.about h2{position:absolute;left:617px;top:860px;font-family:"Orbitron",Arial,sans-serif;font-weight:800;font-size:38px;color:var(--blue)}
.about p{position:absolute;left:611px;top:934px;width:456px;font-size:15px;line-height:18.5px;text-align:justify;color:var(--ink)}
.about .btn{left:613px;top:1141px;width:195px;height:61px;font-size:17px}

/* services */
.services{left:0;top:1306px;width:1200px;height:744px;background:var(--light)}
.eyebrow{position:absolute;left:0;width:1200px;text-align:center;font-family:"Orbitron",Arial,sans-serif;font-weight:800;font-size:18px;color:var(--blue)}
.section-title{position:absolute;left:0;width:1200px;text-align:center;font-family:"Orbitron",Arial,sans-serif;font-weight:800;font-size:31px;color:var(--ink)}
.services .lead{position:absolute;left:0;width:1200px;top:172px;text-align:center;font-size:15px;line-height:18px;color:var(--ink)}
.card{position:absolute;top:246px;width:305px;height:345px;background:var(--white);border-bottom:6px solid var(--navy);box-shadow:0 4px 10px rgba(0,0,0,.12)}
.card .icon{position:absolute;left:32px;top:16px;width:134px;height:150px;background:var(--blue);clip-path:polygon(50% 0,100% 25%,100% 75%,50% 100%,0 75%,0 25%);display:flex;align-items:center;justify-content:center}
.card h3{position:absolute;left:32px;top:182px;font-size:19px;font-weight:500;color:var(--blue-bright)}
.card p{position:absolute;left:30px;top:230px;width:250px;font-size:15px;line-height:18.5px;color:var(--ink)}
.pager{position:absolute;top:654px;display:flex;gap:28px}

/* projects */
.projects{left:0;top:2050px;width:1200px;height:888px;background:linear-gradient(180deg,#6f7276 0%,#9a9b9d 40%,#8c8d8f 75%,#6a6c70 100%)}
.projects .eyebrow{color:var(--white)}
.projects .section-title{color:var(--white)}
.tile{position:absolute}
.projects .btn{left:513px;top:759px;width:172px;height:57px}

/* blog */
.eyebrow-lines{display:flex;justify-content:center;align-items:center;gap:10px}
.eyebrow-lines::before,.eyebrow-lines::after{content:"";width:22px;height:2px;background:var(--blue)}
.post-img{position:absolute}
.post-card{position:absolute;background:var(--white);box-shadow:0 4px 12px rgba(0,0,0,.12)}
.post-card .date{position:absolute;width:70px;height:68px;background:var(--navy);color:var(--white);text-align:center;font-weight:500}
.post-card .date b{display:block;font-size:14px;margin-top:12px;font-weight:500}
.post-card .date span{display:block;font-size:19px}
.post-card .rule{position:absolute;width:2px;background:var(--navy)}
.post-card h3{position:absolute;font-family:"Orbitron",Arial,sans-serif;font-weight:800;font-size:18px;line-height:24px;color:var(--ink)}
.post-card p{position:absolute;font-size:14.5px;line-height:18.5px;color:var(--ink)}
.round-arrows{position:absolute;left:552px;top:3867px;display:flex;gap:10px}

/* quote */
.quote{left:0;top:3953px;width:1200px;height:486px;background:linear-gradient(180deg,#1565c4 0%,#1f6fc4 50%,#2a6aa8 100%)}
.quote h2{position:absolute;left:0;width:1200px;top:60px;text-align:center;font-family:"Orbitron",Arial,sans-serif;font-weight:800;font-size:33px;color:var(--white)}
.field{position:absolute;background:var(--white);font-size:17px;color:#b5b5b5;padding:15px 18px}
.quote .submit{position:absolute;left:521px;top:382px;width:157px;height:61px;background:var(--grey-btn);color:var(--white);font-size:21px;font-weight:500;display:flex;align-items:center;justify-content:center}

/* footer */
.site-footer{left:0;top:4439px;width:1200px;height:439px;background:linear-gradient(180deg,#666 0%,#555 100%)}
.footer-brand{position:absolute;left:0;width:1200px;top:140px;text-align:center;font-family:"Orbitron",Arial,sans-serif;font-weight:800;font-size:23px;line-height:30px;color:var(--white)}
.contact-box{position:absolute;top:229px;height:122px;border:1px solid rgba(255,255,255,.18);display:flex;align-items:center;gap:18px;padding-left:22px;color:var(--white)}
.contact-box .ic{width:78px;height:78px;border-radius:50%;border:3px solid var(--white);display:flex;align-items:center;justify-content:center;flex-shrink:0}
.contact-box small{display:block;font-size:14px}
.contact-box span{font-size:17px;line-height:21px}
.copyright{position:absolute;left:0;width:1200px;top:386px;text-align:center;font-size:13px;color:var(--white)}
</style>
</head>
<body>

<header class="site-header">
  <div class="abs call">CALL US: 555 014 2280</div>
  <div class="btn quote-btn">GET A QUOTE</div>
  <nav class="abs nav nav-left"><span class="active">HOME</span><span>ABOUT US</span><span>CONTACT</span></nav>
  <nav class="abs nav nav-right"><span>SERVICES</span><span>PROJECT</span><span>BLOG</span></nav>
</header>
<div class="brand-tab"><div class="brand-name">HALVERN RIDGE<br>CONSTRUCTION</div></div>

<section class="abs hero" role="img" aria-label="Photo of construction workers in hard hats and high-visibility vests at a building site with cranes">
  <svg class="arrow" style="left:20px" width="24" height="34" viewBox="0 0 24 34"><path d="M18 4 6 17l12 13" fill="none" stroke="#fff" stroke-width="3"/></svg>
  <svg class="arrow" style="left:1156px" width="24" height="34" viewBox="0 0 24 34"><path d="M6 4l12 13L6 30" fill="none" stroke="#fff" stroke-width="3"/></svg>
  <h1>HALVERN RIDGE<br>CONSTRUCTION</h1>
  <p>Lorem ipsum dolor sit amet, consectetur adipiscing elit, sed do eiusmod tempor<br>incididunt ut labore et dolore magna aliquauis ipsum suspendiss.</p>
  <div class="btn">READ MORE</div>
</section>

<section class="about">
  <div class="abs about-photo" role="img" aria-label="Photo of a building under construction with steel framing"></div>
  <h2>ABOUT US</h2>
  <p>Lorem ipsum is simply placeholder text used across the printing and typesetting trade. It has served as the standard filler text for many years, set by early printers who arranged type into sample pages to show how a finished layout would look. It has lasted through several eras of printing, moving from metal type into digital typesetting while remaining largely the same. It became widely used again when layout sheets and later desktop publishing tools made it easy to place sample passages in new designs</p>
  <div class="btn">READ MORE</div>
</section>

<section class="abs services">
  <div class="eyebrow" style="top:68px">OUR SERVICES</div>
  <div class="section-title" style="top:110px">WHAT WE CAN OFFER YOU</div>
  <p class="lead">Lorem ipsum dolor sit amet, consectetur adipiscing elit, sed do eiusmod tempor incididunt ut<br>viverra maecenas accumsan lacus vel facilisis.</p>

  <div class="card" style="left:112px">
    <div class="icon"><svg width="64" height="64" viewBox="0 0 64 64" fill="none" stroke="#fff" stroke-width="3"><path d="M20 12l26 26M44 12 18 38M12 48h18l10-6"/><path d="M8 52h10v-8H8z"/></svg></div>
    <h3>Lorem Ipsum</h3>
    <p>Lorem ipsum dolor sit amet, cons adipiscing elit, sed do eiusmod te incididunt ut labore et dolore ma aliqua. Quis ipsum</p>
  </div>
  <div class="card" style="left:446px">
    <div class="icon"><svg width="64" height="64" viewBox="0 0 64 64" fill="none" stroke="#fff" stroke-width="3"><path d="M10 54h44M16 54V26h14v28M30 54V12h18v42"/><path d="M36 20h6M36 28h6M36 36h6M21 34h4M21 42h4"/></svg></div>
    <h3>Lorem Ipsum</h3>
    <p>Lorem ipsum dolor sit amet, cons adipiscing elit, sed do eiusmod te incididunt ut labore et dolore ma aliqua. Quis ipsum</p>
  </div>
  <div class="card" style="left:780px">
    <div class="icon"><svg width="64" height="64" viewBox="0 0 64 64" fill="none" stroke="#fff" stroke-width="3"><path d="M14 56V14h36v42M10 56h44M20 22h24M20 30h24M20 38h24M20 46h24"/></svg></div>
    <h3>Lorem Ipsum</h3>
    <p>Lorem ipsum dolor sit amet, cons adipiscing elit, sed do eiusmod te incididunt ut labore et dolore ma aliqua. Quis ipsum</p>
  </div>

  <div class="pager" style="left:562px">
    <svg width="18" height="30" viewBox="0 0 18 30"><path d="M14 3 4 15l10 12" fill="none" stroke="#111" stroke-width="3"/></svg>
    <svg width="18" height="30" viewBox="0 0 18 30"><path d="M4 3l10 12L4 27" fill="none" stroke="#111" stroke-width="3"/></svg>
  </div>
</section>

<section class="abs projects" role="img" aria-label="Faded background photo of workers pouring concrete">
  <div class="eyebrow" style="top:52px">PROJECTS</div>
  <div class="section-title" style="top:90px">FEATURED WORKS</div>

  <div class="tile" style="left:110px;top:195px;width:643px;height:242px;background:linear-gradient(135deg,#1f4f86,#2a5f97 50%,#163e6c)" role="img" aria-label="Photo of a worker leveling concrete, tinted blue">
    <svg style="position:absolute;left:292px;top:92px" width="60" height="60" viewBox="0 0 60 60" fill="none" stroke="#fff" stroke-width="3"><circle cx="25" cy="25" r="19"/><path d="M25 15v20M15 25h20M39 39l16 16"/></svg>
  </div>
  <div class="tile" style="left:769px;top:195px;width:316px;height:242px;background:linear-gradient(135deg,#b7a892,#8f7b63 55%,#6d6456)" role="img" aria-label="Photo of two site engineers reviewing plans"></div>
  <div class="tile" style="left:110px;top:453px;width:316px;height:244px;background:linear-gradient(135deg,#a9adb2,#7d7f7a 55%,#5f6158)" role="img" aria-label="Photo of workers walking across a construction site"></div>
  <div class="tile" style="left:439px;top:453px;width:316px;height:244px;background:linear-gradient(135deg,#9fb3c6,#7a7e86 55%,#8a6a50)" role="img" aria-label="Photo of scaffolding around a building under construction"></div>
  <div class="tile" style="left:769px;top:453px;width:316px;height:244px;background:linear-gradient(135deg,#c58a3e,#a86a2c 55%,#6e4a2a)" role="img" aria-label="Photo of hard hats and plans on a desk"></div>

  <div class="btn">MORE</div>
</section>

<section class="blog">
  <div class="abs eyebrow eyebrow-lines" style="top:2983px">BLOG</div>
  <div class="abs section-title" style="top:3018px">LATEST NEWS</div>

  <div class="post-img" style="left:110px;top:3114px;width:534px;height:265px;background:linear-gradient(135deg,#8fb5d8,#a5b9c4 50%,#b9b15a)" role="img" aria-label="Photo of site workers with hard hats near a tower crane"></div>
  <article class="post-card" style="left:619px;top:3148px;width:470px;height:267px">
    <div class="date" style="left:36px;top:-13px"><b>22</b><span>Jan</span></div>
    <div class="rule" style="left:70px;top:55px;height:212px"></div>
    <h3 style="left:132px;top:26px;width:300px">Lorem ipsum dolor sit amet, consectetur</h3>
    <p style="left:136px;top:96px;width:292px">Lorem ipsum dolor sit amet, consectet adipiscing elit, sed do eiusmod tempor incididunt ut labore et dolore magna al Quis ipsum suspendisse ultrices gravid accumsan lacus vel facilisis.</p>
  </article>

  <div class="post-img" style="left:557px;top:3500px;width:532px;height:265px;background:linear-gradient(135deg,#3a3e48,#7a5a3c 50%,#f0a13a 70%,#2e2a28)" role="img" aria-label="Photo of workers silhouetted against a sunset at a steel structure"></div>
  <article class="post-card" style="left:110px;top:3521px;width:467px;height:278px">
    <div class="date" style="left:36px;top:-2px"><b>22</b><span>Jan</span></div>
    <div class="rule" style="left:70px;top:66px;height:212px"></div>
    <h3 style="left:132px;top:36px;width:290px">Lorem ipsum dolor sit amet, consectetur</h3>
    <p style="left:136px;top:106px;width:292px">Lorem ipsum dolor sit amet, consectet adipiscing elit, sed do eiusmod tempor incididunt ut labore et dolore magna al Quis ipsum suspendisse ultrices gravid accumsan lacus vel facilisis.</p>
  </article>

  <div class="round-arrows">
    <svg width="42" height="42" viewBox="0 0 42 42"><circle cx="21" cy="21" r="21" fill="#1a5fc2"/><path d="M24 12l-9 9 9 9" fill="none" stroke="#fff" stroke-width="3"/></svg>
    <svg width="42" height="42" viewBox="0 0 42 42"><circle cx="21" cy="21" r="21" fill="#1a5fc2"/><path d="M18 12l9 9-9 9" fill="none" stroke="#fff" stroke-width="3"/></svg>
  </div>
</section>

<section class="abs quote" role="img" aria-label="Blue-tinted background photo of a worker on site">
  <h2>GET A QUOTE</h2>
  <div class="field" style="left:328px;top:130px;width:263px;height:53px">Name :</div>
  <div class="field" style="left:600px;top:130px;width:263px;height:53px">Phone :</div>
  <div class="field" style="left:328px;top:202px;width:263px;height:53px">Email :</div>
  <div class="field" style="left:600px;top:202px;width:263px;height:53px">Subject:</div>
  <div class="field" style="left:328px;top:272px;width:535px;height:150px">Message :</div>
  <div class="submit">SUBMIT</div>
</section>

<footer class="abs site-footer">
  <div class="footer-brand">HALVERN RIDGE<br>CONSTRUCTION</div>

  <div class="contact-box" style="left:110px;width:340px">
    <div class="ic"><svg width="34" height="40" viewBox="0 0 34 40"><path d="M17 2C9 2 3 8 3 16c0 10 14 22 14 22s14-12 14-22C31 8 25 2 17 2z" fill="#fff"/><circle cx="17" cy="16" r="5" fill="#555"/></svg></div>
    <span>Halvern 41-208/street<br>loreroad</span>
  </div>
  <div class="contact-box" style="left:455px;width:355px">
    <div class="ic"><svg width="38" height="28" viewBox="0 0 38 28"><rect x="1" y="1" width="36" height="26" rx="2" fill="#fff"/><path d="M2 3l17 13L36 3" fill="none" stroke="#555" stroke-width="2.5"/></svg></div>
    <div><small>Email</small><span>hello@halvernridge.example</span></div>
  </div>
  <div class="contact-box" style="left:814px;width:303px">
    <div class="ic"><svg width="36" height="36" viewBox="0 0 36 36"><path d="M8 2l7 8-4 5c2 4 6 8 10 10l5-4 8 7-4 6C17 34 2 19 2 6z" fill="#fff"/></svg></div>
    <div><small>Phone</small><span style="font-size:20px">(555)-0142280</span></div>
  </div>

  <div class="copyright">Copyright © 2022 · HALVERN RIDGE CONSTRUCTION</div>
</footer>

</body>
</html>
```